Detail Shop Menu Board for Walk In Clients

I am looking to have digital menus for my detail shop. I have 3 55-inch TVs on the wall for my front desk area. They will be vertical on the wall, not horizontal, so the design needs to be vertical.

Color pallet I am looking for is black and gold, with some accent colors if applicable. I would like black background with some sort of design in it in such a way it looks faint or ghosted in the background ... i.e., honeycomb, splatter, etc. A boarder is optional.

Needs to be designed well, organized well and easy to read for customers walking in.

the each category is for each TV: Interior and Maintenance plans, Exterior and Ceramic Coatings

Company logo files included. would like my logos on them as well.

This job will need another menu board done in the future as well.

Industry/Entity Type

Auto Detailing

Requirements
Should not have
• no dollar signs ($) on any pricing

```html
<!DOCTYPE html>
<html lang="en">
<head>
<meta charset="utf-8">
<title>Detail Shop Menu Boards</title>
<link rel="stylesheet" href="https://fonts.googleapis.com/css2?family=Archivo+Black&family=Poppins:wght@400;500;600;700;800&display=swap">
<style>
:root{
  --page:#ffffff;
  --board:#0b0b0b;
  --panel-top:#0e0e0e;
  --panel-bottom:#262626;
  --gold-light:#f3e3a2;
  --gold:#c9a650;
  --gold-dark:#8d6c24;
  --ink:#111111;
  --text:#f2f2f2;
  --muted:#c9c9c9;
  --rule:#7d6530;
  --gold-fill:linear-gradient(180deg,#ecd998 0%,#d2b462 45%,#9c7a2e 100%);
  --gold-text:linear-gradient(180deg,#eddb96 0%,#cda955 50%,#8f6e28 100%);
}
*{margin:0;padding:0;box-sizing:border-box}
html,body{width:1200px;height:2166px;overflow:hidden;background:var(--page)}
body{font-family:'Poppins',sans-serif;color:var(--text)}
.stage{position:absolute;left:0;top:0;width:1418px;height:2560px;transform:scale(0.84626);transform-origin:0 0}
.board{position:absolute;width:584px;height:1152px;background:var(--board);overflow:hidden}
.board-exterior{left:108px;top:113px}
.board-interior{left:744px;top:113px}
.board-ceramic{left:400px;top:1314px}
.abs{position:absolute}
.ghost-pattern{position:absolute;left:0;right:0;bottom:0;height:260px;background:radial-gradient(ellipse at 50% 100%,rgba(120,85,30,.35),rgba(0,0,0,0) 70%)}
.brand{position:absolute;left:45px;top:70px;width:125px;text-align:center;font-weight:700;font-size:15px;line-height:18px;color:var(--text);letter-spacing:1px}
.brand-dot{width:34px;height:34px;border-radius:50%;border:2px solid var(--text);margin:0 auto 8px}
.title{position:absolute;left:245px;top:40px;width:300px}
.title-line{display:block;white-space:nowrap;font-family:'Archivo Black',sans-serif;font-size:61px;line-height:54px;background:var(--gold-text);-webkit-background-clip:text;background-clip:text;color:transparent;transform:scaleX(.76);transform-origin:0 0;width:395px}
.title-ceramic .title-line{transform:scaleX(.87);width:350px}
.title-sub{font-weight:700;font-size:30px;line-height:36px;color:#fff;margin-top:2px}
.rule{position:absolute;left:45px;width:498px;height:1px;background:var(--rule)}
.panel{position:absolute;left:44px;width:499px;border-radius:8px;background:linear-gradient(180deg,var(--panel-top),var(--panel-bottom))}
.label{position:absolute;left:62px;font-weight:700;font-size:12px;line-height:14px;color:#fff}
.label .arrow{display:inline-block;margin-left:6px;border-left:5px solid #fff;border-top:4px solid transparent;border-bottom:4px solid transparent;vertical-align:1px}
.col-head{position:absolute;width:90px;text-align:center;font-size:11.5px;font-weight:500;color:#fff}
.pill{position:absolute;height:34px;border-radius:5px;background:var(--gold-fill);color:var(--ink);display:flex;align-items:center;justify-content:center;font-weight:700;font-size:26px;line-height:1}
.pill .note{font-size:6.5px;line-height:6.5px;font-weight:800;margin-left:3px;text-align:left}
.features{position:absolute;list-style:none;font-size:9.3px;line-height:14.6px;color:var(--muted)}
.features li{position:relative;padding-left:13px}
.features li::before{content:"✓";position:absolute;left:0;top:3px;width:8px;height:8px;border:1px solid var(--muted);border-radius:1px;font-size:7px;line-height:7px;text-align:center;color:var(--gold-light)}
.features li.wrap{line-height:10.5px;padding-top:2px;padding-bottom:2px}
.center{text-align:center}
.section-title{position:absolute;left:0;width:584px;text-align:center;font-weight:800;font-size:22px;background:var(--gold-text);-webkit-background-clip:text;background-clip:text;color:transparent}
.white-head{position:absolute;left:0;width:584px;text-align:center;font-weight:700;font-size:14px;color:#fff}
.polish-frame{position:absolute;left:45px;top:718px;width:498px;height:196px;border:1px solid var(--rule);border-radius:4px}
.polish-title{position:absolute;left:140px;top:703px;width:304px;background:var(--board);text-align:center;font-weight:800;font-size:21px;line-height:28px;background-image:var(--gold-text);-webkit-background-clip:text;background-clip:text;color:transparent}
.polish-title-bg{position:absolute;left:140px;top:710px;width:304px;height:16px;background:var(--board)}
.plain-price{position:absolute;width:110px;text-align:center;font-weight:700;font-size:28px;line-height:30px;background:var(--gold-text);-webkit-background-clip:text;background-clip:text;color:transparent}
.plain-price .note{font-size:6.5px;line-height:6.5px;display:inline-block;color:#fff;-webkit-text-fill-color:#fff;vertical-align:6px;text-align:left}
.vdiv{position:absolute;width:1px;background:var(--rule)}
.spaced{position:absolute;left:0;width:584px;text-align:center;font-size:11px;letter-spacing:3px;color:var(--gold);font-weight:500}
.quote-line{position:absolute;left:132px;top:905px;width:320px;background:var(--board);text-align:center;font-size:11px;line-height:18px;color:#fff}
.quote-line b{font-weight:700}
.addon-band{position:absolute;left:0;top:990px;width:584px;height:162px;border-radius:30px 30px 0 0;background:linear-gradient(90deg,#8a6a22 0%,#cdb060 25%,#f3e3a2 55%,#d8ba64 80%,#8d6c24 100%)}
.addon{position:absolute;top:1020px;width:112px;text-align:center;color:var(--ink)}
.addon-name{font-weight:700;font-size:11.5px;line-height:13px}
.addon-desc{font-size:6.6px;line-height:8px;margin-top:1px}
.addon-price{font-weight:700;font-size:22px;line-height:24px;margin-top:10px}
.addon-price .note{font-size:6.5px;line-height:6.5px;display:inline-block;vertical-align:6px;text-align:left;font-weight:800}
.band-div{position:absolute;top:1015px;width:1px;height:115px;background:rgba(60,45,10,.45)}
.rate-box{position:absolute;left:306px;width:236px;height:34px;border:1px solid #8a7a55;border-radius:5px}
.rate-label{position:absolute;left:16px;top:10px;font-size:9.5px;font-weight:700;color:#fff}
.rate-value{position:absolute;right:-1px;top:-1px;width:87px;height:34px;border-radius:5px;background:var(--gold-fill);color:var(--ink);display:flex;align-items:center;justify-content:center;font-weight:700;font-size:26px}
.rate-value .note{font-size:6.3px;line-height:6.3px;font-weight:800;margin-left:4px;text-align:left}
.tile{position:absolute;top:581px;width:86px;height:64px;border-radius:4px;background:var(--gold-fill);color:var(--ink);text-align:center;padding-top:5px}
.tile-name{font-weight:700;font-size:11px;line-height:11.5px}
.tile-price{font-weight:700;font-size:23px;line-height:26px}
.tile-price .note{font-size:7px;line-height:7px;display:inline-block;text-align:left;font-weight:500;vertical-align:4px}
.plan-intro{position:absolute;left:50px;top:730px;width:484px;text-align:center;font-size:8.8px;line-height:11px;color:#e6e6e6}
.bespoke{position:absolute;left:0;top:216px;width:584px;text-align:center;font-weight:800;font-size:28px;line-height:32px;background:var(--gold-text);-webkit-background-clip:text;background-clip:text;color:transparent}
.package-word{position:absolute;left:0;top:250px;width:584px;text-align:center;font-size:17px;letter-spacing:9px;color:#fff}
.starting{position:absolute;left:0;top:280px;width:584px;text-align:center;font-weight:600;font-size:14px;color:#fff}
.tagline{position:absolute;left:221px;top:366px;width:142px;background:var(--board);text-align:center;font-size:11px;color:#fff}
.tagline b{color:var(--gold);font-weight:700}
.tier{position:absolute;top:437px;width:142px;height:255px;border-radius:6px;background:linear-gradient(180deg,#1a1a1a,#262626)}
.tier-badge{height:36px;border-radius:5px;text-align:center;font-weight:700;font-size:10.5px;line-height:11px;padding-top:7px}
.tier-platinum .tier-badge{background:linear-gradient(180deg,#3a3a3a,#1d1d1d);color:#e8e8e8}
.tier-gold .tier-badge{background:var(--gold-fill);color:var(--ink)}
.tier-entry .tier-badge{background:linear-gradient(180deg,#f0f0f0,#a9a9a9);color:var(--ink)}
.tier-row{position:absolute;left:16px;font-size:9.5px;line-height:10px;color:#fff}
.tier .pill{left:67px;width:60px;height:26px;font-size:20px;border-radius:3px}
.tier-desc{position:absolute;left:12px;top:150px;width:118px;text-align:center;font-size:9px;line-height:10.6px;color:#ddd}
.other{position:absolute;top:790px;width:170px;text-align:center}
.other-icon{height:34px;display:flex;justify-content:center;align-items:center}
.other-name{font-weight:700;font-size:10.5px;margin-top:6px;color:#fff}
.other .pill{position:relative;margin:8px auto 0;width:74px;height:30px;font-size:22px;border-radius:4px}
.per-wheel{font-weight:700;font-size:8.5px;margin-top:7px;color:#fff}
.other-desc{font-size:9px;line-height:10.6px;margin:20px auto 0;width:128px;color:#ddd}
</style>
</head>
<body>
<div class="stage">

  <section class="board board-exterior">
    <div class="ghost-pattern" role="img" aria-label="Faint honeycomb texture glowing gold behind the add-on area" style="bottom:140px;height:160px"></div>
    <div class="brand"><div class="brand-dot"></div>EMBER FORGE<br>GARAGE</div>
    <div class="title">
      <div class="title-line">EXTETIOR</div>
      <div class="title-line">DETAILING</div>
      <div class="title-sub">PACKAGES</div>
    </div>
    <div class="rule" style="top:188px"></div>

    <div class="panel" style="top:222px;height:123px"></div>
    <div class="label" style="top:259px">BASIC EXTERIOR DETAIL<span class="arrow"></span></div>
    <div class="col-head" style="left:243px;top:234px">Cars</div>
    <div class="col-head" style="left:341px;top:234px">Midsize</div>
    <div class="col-head" style="left:439px;top:234px">Trucks/SUVs</div>
    <div class="pill" style="left:245px;top:251px;width:85px">100</div>
    <div class="pill" style="left:343px;top:251px;width:85px">125</div>
    <div class="pill" style="left:441px;top:251px;width:86px">150<span class="note">AND<br>UP<br>+TAX</span></div>
    <ul class="features" style="left:62px;top:300px"><li>Standard Hand wash</li><li>Wheels/Wheel wells cleaned</li></ul>
    <ul class="features" style="left:245px;top:300px"><li>Exterior plastics dressing</li><li>Tire dressing</li></ul>
    <ul class="features" style="left:410px;top:300px"><li>Window cleaning</li><li>Spray wax</li></ul>

    <div class="panel" style="top:367px;height:156px"></div>
    <div class="label" style="top:402px">COMPLETE EXTERIOR<span class="arrow" style="margin-left:16px"></span><br>DETAIL</div>
    <div class="col-head" style="left:243px;top:378px">Cars</div>
    <div class="col-head" style="left:341px;top:378px">Midsize</div>
    <div class="col-head" style="left:439px;top:378px">Trucks/SUVs</div>
    <div class="pill" style="left:245px;top:395px;width:85px">180</div>
    <div class="pill" style="left:343px;top:395px;width:85px">220</div>
    <div class="pill" style="left:441px;top:395px;width:86px">260<span class="note">AND<br>UP<br>+TAX</span></div>
    <ul class="features" style="left:62px;top:444px;width:170px"><li>Standard hand wash</li><li>Iron decontamination</li><li class="wrap">Clay bar treatment to remove environmental contamination (sap, tar, etc),</li></ul>
    <ul class="features" style="left:245px;top:444px;width:150px"><li class="wrap">Tires, wheels, wheel wells cleaned and dressed</li><li>Door jams cleaned</li><li class="wrap">Trunk lid/Rear Hatch, gas cap area cleaned</li></ul>
    <ul class="features" style="left:410px;top:444px"><li>Exterior glass cleaned</li><li>Black plastics dressed</li><li>SiO2 protection</li></ul>

    <div class="panel" style="top:550px;height:118px"></div>
    <div class="label" style="top:586px">EXECUTIVE EXTERIOR<span class="arrow" style="margin-left:12px"></span><br>DETAIL &amp; EXPRESS<br>COATING</div>
    <div class="col-head" style="left:243px;top:561px">Cars</div>
    <div class="col-head" style="left:341px;top:561px">Midsize</div>
    <div class="col-head" style="left:439px;top:561px">Trucks/SUVs</div>
    <div class="pill" style="left:245px;top:577px;width:85px">350</div>
    <div class="pill" style="left:343px;top:577px;width:85px">400</div>
    <div class="pill" style="left:441px;top:577px;width:86px">450<span class="note">AND<br>UP<br>+TAX</span></div>
    <ul class="features" style="left:62px;top:638px"><li>Complete Exterior Detail PLUS 1yr Ceramic Coating</li></ul>

    <div class="polish-frame"></div>
    <div class="polish-title-bg"></div>
    <div class="polish-title">POLISHING &amp; PAINTWORK</div>
    <div class="white-head" style="top:742px;font-size:12px">EXTERIOR ENHANCEMENT DETAIL</div>
    <div class="col-head" style="left:118px;top:771px">Cars</div>
    <div class="col-head" style="left:243px;top:771px">Midsize</div>
    <div class="col-head" style="left:375px;top:771px">Trucks/SUVs</div>
    <div class="plain-price" style="left:108px;top:786px">350</div>
    <div class="plain-price" style="left:233px;top:786px">400</div>
    <div class="plain-price" style="left:370px;top:786px">450 <span class="note">AND<br>UP<br>+TAX</span></div>
    <div class="vdiv" style="left:226px;top:775px;height:38px"></div>
    <div class="vdiv" style="left:353px;top:775px;height:38px"></div>
    <div class="spaced" style="top:833px">OUR COMPLETE EXTERIOR PACKAGE PLUS:</div>
    <ul class="features" style="left:95px;top:854px"><li>Single step polish</li><li>Upgraded paint sealant</li></ul>
    <ul class="features" style="left:257px;top:854px"><li>Upgraded durable, long-lasting tire and trim dressing</li><li>Windshield Protection</li></ul>
    <div class="quote-line"><b>Exterior Multi-Step Paint Correction:</b> Price By Quote Only</div>

    <div class="white-head" style="top:958px;font-size:17px">EXTERIOR ADD ON’S</div>
    <div class="addon-band"></div>
    <div class="addon" style="left:66px">
      <div class="addon-name">Complete Wheel<br>Detail</div>
      <div class="addon-desc">Wheels off, deep cleaned<br>and protected inside and<br>out, reinstalled and torqued<br>to factory spec</div>
      <div class="addon-price" style="margin-top:2px">150<span class="note">AND<br>UP</span></div>
    </div>
    <div class="band-div" style="left:192px"></div>
    <div class="addon" style="left:193px">
      <div class="addon-name">Headlight<br>Restoration</div>
      <div class="addon-price">100<span class="note">AND<br>UP</span></div>
    </div>
    <div class="band-div" style="left:307px"></div>
    <div class="addon" style="left:307px">
      <div class="addon-name">Water Spot<br>Removal</div>
      <div class="addon-price">50<span class="note">AND<br>UP</span></div>
    </div>
    <div class="band-div" style="left:419px"></div>
    <div class="addon" style="left:421px">
      <div class="addon-name">Plastic Trim<br>Restoration</div>
      <div class="addon-price">50<span class="note">AND<br>UP</span></div>
    </div>
  </section>

  <section class="board board-interior">
    <div class="ghost-pattern" role="img" aria-label="Faint honeycomb texture glowing gold along the bottom"></div>
    <div class="brand"><div class="brand-dot"></div>EMBER FORGE<br>GARAGE</div>
    <div class="title">
      <div class="title-line">INTERIOR</div>
      <div class="title-line">DETAILING</div>
      <div class="title-sub">PACKAGES</div>
    </div>
    <div class="rule" style="top:188px"></div>

    <div class="label" style="left:46px;top:230px">DELUXE INTERIOR CLEAN<span class="arrow" style="margin-left:12px"></span></div>
    <div class="rate-box" style="top:220px"><span class="rate-label">HOURLY SHOP RATE AT</span><div class="rate-value">85<span class="note">PER<br>HOUR<br>(+TAX)</span></div></div>
    <ul class="features" style="left:46px;top:265px"><li>Full vacuum of carpet, seats, upholstery</li><li>Floormats treated and steam cleaned</li><li>Dash/doors scrubbed, wiped down and dressed</li><li>Clean console, cup holders, crevices and vents</li><li>Clean dash and UV protectant</li><li>Clean all interior trim and plastics</li><li>Clean and condition door panels and pockets</li></ul>
    <ul class="features" style="left:306px;top:265px"><li>Clean door jambs and weather stripping</li><li>Clean glass surfaces</li><li>Lightly clean vehicle headliner and sun visors</li><li>Shampoo cloth seats</li><li>Deep clean and condition leather seats</li><li>Apply protective treatment to leather and vinyl</li><li>Trunk and spare tire areas also cleaned</li></ul>
    <div class="rule" style="top:388px"></div>

    <div class="label" style="left:46px;top:422px">BASIC INTERIOR CLEAN<span class="arrow" style="margin-left:22px"></span></div>
    <div class="rate-box" style="top:412px"><span class="rate-label">HOURLY SHOP RATE AT</span><div class="rate-value">85<span class="note">PER<br>HOUR<br>(+TAX)</span></div></div>
    <ul class="features" style="left:46px;top:456px"><li>Full vacuum of carpet, seats, upholstery</li><li>Floormats treated and steam cleaned</li><li>Dash/doors lightly wiped down and dressed</li></ul>
    <ul class="features" style="left:306px;top:456px;width:236px"><li>Interior glass surfaces cleaned</li><li class="wrap">Steering wheel and center console scrubbed and cleaned</li></ul>
    <div class="rule" style="top:525px"></div>

    <div class="white-head" style="top:547px;font-size:15px">INTERIOR ADD ON’S</div>
    <div class="tile" style="left:126px"><div class="tile-name">Ozone<br>Treatment</div><div class="tile-price">50</div></div>
    <div class="tile" style="left:250px"><div class="tile-name">Fabric<br>Guard</div><div class="tile-price">100<span class="note">PER<br>ROW</span></div></div>
    <div class="tile" style="left:369px"><div class="tile-name">BioHazard<br>Cleaning</div><div class="tile-price">500<span class="note">PER<br>ROW</span></div></div>
    <div class="rule" style="top:673px"></div>

    <div class="section-title" style="top:694px">MAINTENANCE PLANS</div>
    <div class="plan-intro">All maintenance plans start with a Complete Exterior Detail and Deluxe Interior Detail to provide a clean, fresh start. After that has been performed, we will schedule you for your follow up maintenance program.</div>

    <div class="panel" style="top:775px;height:143px"></div>
    <div class="label" style="top:803px">MONTHLY<span class="arrow" style="margin-left:90px"></span><br>MAINTENANCE DETAIL</div>
    <div class="col-head" style="left:243px;top:778px">Cars</div>
    <div class="col-head" style="left:341px;top:778px">Midsize</div>
    <div class="col-head" style="left:439px;top:778px">Trucks/SUVs</div>
    <div class="pill" style="left:245px;top:795px;width:85px">100</div>
    <div class="pill" style="left:343px;top:795px;width:85px">125</div>
    <div class="pill" style="left:441px;top:795px;width:86px">150<span class="note">AND<br>UP<br>+TAX</span></div>
    <ul class="features" style="left:62px;top:848px"><li>Pre rinse</li><li>Hand wash</li><li>Wheels/Wheel wells cleaned</li><li>Exterior plastics dressing</li></ul>
    <ul class="features" style="left:245px;top:848px"><li>Tire dressing</li><li>Window cleaning</li><li>Spray on protection</li><li>Interior vacuum</li></ul>
    <ul class="features" style="left:410px;top:848px;width:120px"><li class="wrap">Interior wiped down &amp; dressing</li><li>All Glass cleaned</li></ul>

    <div class="panel" style="top:945px;height:147px"></div>
    <div class="label" style="top:972px">BI-MONTHLY<span class="arrow" style="margin-left:72px"></span><br>MAINTENANCE DETAIL</div>
    <div class="col-head" style="left:243px;top:947px">Cars</div>
    <div class="col-head" style="left:341px;top:947px">Midsize</div>
    <div class="col-head" style="left:439px;top:947px">Trucks/SUVs</div>
    <div class="pill" style="left:245px;top:964px;width:85px">150</div>
    <div class="pill" style="left:343px;top:964px;width:85px">175</div>
    <div class="pill" style="left:441px;top:964px;width:86px">200<span class="note">AND<br>UP<br>+TAX</span></div>
    <ul class="features" style="left:62px;top:1015px"><li>Pre rinse</li><li>Hand wash</li><li>Bug/Tar Removal</li><li>Wheels/Wheel wells cleaned</li></ul>
    <ul class="features" style="left:225px;top:1015px"><li>Exterior plastics dressing</li><li>Tire dressing</li><li>Window cleaning</li><li>Spray on protection</li></ul>
    <ul class="features" style="left:368px;top:1015px"><li>Interior vacuum</li><li>Interior wiped down &amp; dressing</li><li>Spot Treatment for Stains, etc</li><li>All Glass cleaned</li></ul>
  </section>

  <section class="board board-ceramic">
    <div class="ghost-pattern" role="img" aria-label="Faint honeycomb texture glowing gold along the bottom"></div>
    <div class="brand"><div class="brand-dot"></div>EMBER FORGE<br>GARAGE</div>
    <div class="title title-ceramic" style="left:243px">
      <div class="title-line">CERAMIC</div>
      <div class="title-line">COATINGS</div>
    </div>
    <div class="rule" style="top:188px"></div>

    <div class="bespoke">BESPOKE CERAMIC COATING</div>
    <div class="package-word">PACKAGE</div>
    <div class="starting">Starting at</div>
    <div class="pill" style="left:241px;top:302px;width:102px;height:40px;font-size:30px">3000</div>
    <div class="rule" style="top:375px"></div>
    <div class="tagline">ONE WORD: <b>PERFECTION</b></div>

    <div class="tier tier-platinum" style="left:54px">
      <div class="tier-badge">PLATINUM LEVEL<br>COATING</div>
      <div class="tier-row" style="top:64px">Cars</div><div class="pill" style="top:56px">1300</div>
      <div class="tier-row" style="top:92px">Midsize</div><div class="pill" style="top:84px">1500</div>
      <div class="tier-row" style="top:114px">Trucks/<br>SUVs</div><div class="pill" style="top:112px">1700<span class="note">AND<br>UP<br>+TAX</span></div>
      <div class="tier-desc">Warrantied paint coating, applied to all painted surfaces, plastic trim, and wheel faces. provides up to 60 months (50-60k miles) of durability when maintained properly</div>
    </div>
    <div class="tier tier-gold" style="left:224px">
      <div class="tier-badge">GOLD LEVEL<br>COATING</div>
      <div class="tier-row" style="top:64px">Cars</div><div class="pill" style="top:56px">900</div>
      <div class="tier-row" style="top:92px">Midsize</div><div class="pill" style="top:84px">1000</div>
      <div class="tier-row" style="top:114px">Trucks/<br>SUVs</div><div class="pill" style="top:112px">1100<span class="note">AND<br>UP<br>+TAX</span></div>
      <div class="tier-desc">Durable paint coating applied to all painted surfaces and plastic trim, provides up to 36 months (30-36k miles) of durability when maintained properly</div>
    </div>
    <div class="tier tier-entry" style="left:388px">
      <div class="tier-badge">ENTRY LEVEL<br>COATING</div>
      <div class="tier-row" style="top:64px">Cars</div><div class="pill" style="top:56px">600</div>
      <div class="tier-row" style="top:92px">Midsize</div><div class="pill" style="top:84px">700</div>
      <div class="tier-row" style="top:114px">Trucks/<br>SUVs</div><div class="pill" style="top:112px">800<span class="note">AND<br>UP<br>+TAX</span></div>
      <div class="tier-desc">Coating applied to all painted surfaces, provides up to a 12-month (10-12k miles) lifespan of durability. Add a second layer for 100 more for 18-24 months (20k-24k miles) of protection</div>
    </div>

    <div class="rule" style="top:744px"></div>
    <div class="abs" style="left:150px;top:730px;width:284px;height:28px;background:var(--board)"></div>
    <div class="section-title" style="top:727px;font-size:20px">OTHER COATINGS OFFERED</div>

    <div class="vdiv" style="left:210px;top:788px;height:245px"></div>
    <div class="vdiv" style="left:380px;top:788px;height:245px"></div>

    <div class="other" style="left:41px">
      <div class="other-icon"><svg width="32" height="32" viewBox="0 0 32 32"><circle cx="16" cy="16" r="14" fill="none" stroke="#c9a650" stroke-width="3"/><circle cx="16" cy="16" r="8" fill="none" stroke="#c9a650" stroke-width="2"/><circle cx="16" cy="16" r="3" fill="#c9a650"/></svg></div>
      <div class="other-name">WHEEL COATING</div>
      <div class="pill">50<span class="note">AND<br>UP</span></div>
      <div class="per-wheel">PER WHEEL</div>
      <div class="other-desc">Wheel face coated with one layer of ceramic giving you up to 9-12 months of protection. 2 layers will yield 12-18+ months of protection. *Raw aluminum wheels CAN NOT be coated.</div>
    </div>
    <div class="other" style="left:211px">
      <div class="other-icon"><svg width="28" height="34" viewBox="0 0 28 34"><ellipse cx="14" cy="17" rx="12" ry="15" fill="none" stroke="#c9a650" stroke-width="4"/><ellipse cx="14" cy="17" rx="5" ry="8" fill="none" stroke="#c9a650" stroke-width="2"/></svg></div>
      <div class="other-name">WHEEL OFF COATING</div>
      <div class="pill">400<span class="note">AND<br>UP</span></div>
      <div class="per-wheel">PER WHEEL</div>
      <div class="other-desc">Wheel coating package + durable industrial coating on barrels of wheels and if applicable, calipers and suspension components.</div>
    </div>
    <div class="other" style="left:381px">
      <div class="other-icon"><svg width="36" height="26" viewBox="0 0 36 26"><path d="M3 3 H33 L29 23 H7 Z" fill="#c9a650"/><path d="M12 20 L22 7" stroke="#0b0b0b" stroke-width="2"/></svg></div>
      <div class="other-name">WINDSHIELD COATING</div>
      <div class="pill">100<span class="note">AND<br>UP</span></div>
      <div class="per-wheel">PER WHEEL</div>
      <div class="other-desc">Glass is polished to remove any stuck-on contamination and treated with a coating that lasts 6 months to a year+. Lifespan of the coating is in relation to wiper use and environment.</div>
    </div>
  </section>

</div>
</body>
</html>
```